Business Card for New Convenience Store

We need a business card for our new convenience store using our logo. We want to have a color scheme and back ground created that will be transferable to other media platforms and advertising.

Industry/Entity Type

Convenience Store

```html
<!DOCTYPE html>
<html lang="en">
<head>
<meta charset="utf-8">
<title>Cedar Stop – Business Card</title>
<link href="https://fonts.googleapis.com/css2?family=Open+Sans:wght@400;600;700&display=swap" rel="stylesheet">
<style>
  :root {
    --page-bg: #ece7e1;
    --brown-dark: #4e3523;
    --brown-mid: #7a5537;
    --brown-light: #8f6a48;
    --stripe-brown: #8a6446;
    --ink: #1f1f1f;
    --paper: #ffffff;
    --sky: #b9c8dc;
    --facade: #8c6a4c;
  }
  * { margin: 0; padding: 0; box-sizing: border-box; }
  html, body {
    width: 1200px; height: 1000px; overflow: hidden;
    background: var(--page-bg);
    font-family: "Open Sans", Arial, sans-serif;
  }
  .canvas { position: relative; width: 1200px; height: 1000px; }

  .card {
    position: absolute;
    overflow: hidden;
    box-shadow: 0 6px 14px rgba(0,0,0,0.25);
  }
  .card svg { position: absolute; inset: 0; display: block; }

  /* Front */
  .card-front { left: 72px; top: 32px; width: 748px; height: 438px; }
  .front-brand {
    position: absolute; left: 0; right: 0; top: 350px;
    text-align: center;
    color: var(--paper);
    font-weight: 700; font-size: 50px; letter-spacing: 1px;
  }

  /* Back */
  .card-back { left: 422px; top: 518px; width: 750px; height: 437px; background: var(--paper); }
  .contact-name {
    position: absolute; left: 23px; top: 28px;
    font-size: 25px; font-weight: 600; color: var(--ink);
  }
  .contact-role {
    position: absolute; left: 23px; top: 63px;
    font-size: 17px; color: var(--ink);
  }
  .contact-address {
    position: absolute; left: 23px; top: 286px;
    font-size: 17.5px; line-height: 30px; color: var(--paper);
  }
  .contact-line {
    position: absolute; left: 23px;
    display: flex; align-items: center; gap: 10px;
    font-size: 17.5px; color: var(--paper);
  }
  .contact-phone { top: 355px; }
  .contact-email { top: 387px; }
  .contact-line svg { position: static; width: 14px; height: 14px; }
  .back-brand {
    position: absolute; left: 380px; width: 340px; top: 200px;
    text-align: center;
    color: var(--ink);
    font-weight: 700; font-size: 48px; letter-spacing: 1px;
  }
</style>
</head>
<body>
<div class="canvas">

  <section class="card card-front">
    <svg viewBox="0 0 748 438" width="748" height="438">
      <defs>
        <linearGradient id="storefront-tone" x1="0" y1="0" x2="0" y2="1">
          <stop offset="0" stop-color="var(--sky)"/>
          <stop offset="0.35" stop-color="#9aa39a"/>
          <stop offset="0.7" stop-color="var(--facade)"/>
          <stop offset="1" stop-color="#d8d6d2"/>
        </linearGradient>
        <radialGradient id="front-brown" cx="0.5" cy="0.4" r="0.7">
          <stop offset="0" stop-color="var(--brown-light)"/>
          <stop offset="1" stop-color="var(--brown-dark)"/>
        </radialGradient>
      </defs>
      <rect class="store-photo" width="748" height="340" fill="url(#storefront-tone)" role="img" aria-label="Rendering of the new store building with stone entrance, glass front and shoppers walking in"/>
      <path class="wave-white" d="M0,250 C120,292 230,320 360,306 C500,292 620,228 748,218 L748,438 L0,438Z" fill="var(--paper)"/>
      <path class="wave-black" d="M0,258 C120,300 230,328 360,314 C500,300 620,236 748,226" fill="none" stroke="var(--ink)" stroke-width="4"/>
      <path class="wave-brown" d="M0,266 C120,306 230,334 360,322 C500,310 620,244 748,236 L748,438 L0,438Z" fill="url(#front-brown)"/>
    </svg>
    <div class="front-brand">Cedar Stop</div>
  </section>

  <section class="card card-back">
    <svg viewBox="0 0 750 437" width="750" height="437">
      <defs>
        <linearGradient id="back-brown" x1="0" y1="0" x2="0" y2="1">
          <stop offset="0" stop-color="var(--brown-dark)"/>
          <stop offset="0.5" stop-color="var(--brown-light)"/>
          <stop offset="1" stop-color="var(--brown-dark)"/>
        </linearGradient>
      </defs>
      <path class="stripe-black" d="M370,0 C425,80 405,140 355,220 C305,300 355,380 395,437" fill="none" stroke="var(--ink)" stroke-width="5"/>
      <path class="stripe-brown" d="M358,0 C413,80 393,140 343,220 C293,300 343,380 383,437" fill="none" stroke="var(--stripe-brown)" stroke-width="4"/>
      <path class="panel-brown" d="M0,0 L345,0 C400,80 380,140 330,220 C280,300 330,380 370,437 L0,437Z" fill="url(#back-brown)"/>
    </svg>
    <div class="contact-name">Dana Whitfield</div>
    <div class="contact-role">Manager</div>
    <div class="contact-address">412 Cedar Bend Rd.<br>Millbrook, AL 36054</div>
    <div class="contact-line contact-phone">
      <svg viewBox="0 0 16 16" aria-hidden="true"><path d="M2,6 C2,3 14,3 14,6 L11,7 L10,5 L6,5 L5,7Z M4,8 L12,8 L13,13 L3,13Z" fill="#fff"/></svg>
      <span>334-555-0148</span>
    </div>
    <div class="contact-line contact-email">
      <svg viewBox="0 0 16 16" aria-hidden="true"><rect x="1.5" y="3.5" width="13" height="9" fill="none" stroke="#fff" stroke-width="1.2"/><path d="M1.5,3.5 L8,9 L14.5,3.5" fill="none" stroke="#fff" stroke-width="1.2"/></svg>
      <span>dwhitfield@cedarstop.com</span>
    </div>
    <div class="back-brand">Cedar Stop</div>
  </section>

</div>
</body>
</html>
```